Commercial Real Estate

We need a business card design for a new commercial real estate business that specializes in apartment building brokerage. Not individual units but the entire complex. We find and represent the owners existing buildings and well as new buyers for those buildings. The design should convey trust, integrity, knowledge and growth. It should be easily read.

Target Market(s)

40 to 65 years old

Industry/Entity Type

Real Estate

```html
<!DOCTYPE html>
<html lang="en">
<head>
<meta charset="utf-8">
<title>Landmere Property Investments – Business Card</title>
<link rel="stylesheet" href="https://fonts.googleapis.com/css2?family=Arimo:wght@400;700&display=swap">
<style>
  :root {
    --page-bg: #d9dadc;
    --teal-top: #6fa9a8;
    --teal-mid: #6dcaca;
    --teal-low: #62b3b1;
    --teal-deep: #4d7d7a;
    --teal-accent: #4fc0bf;
    --ink: #4a5355;
    --ink-soft: #3f4749;
    --card-white: #ffffff;
    --logo-ink: #4b5a5b;
  }
  * { margin: 0; padding: 0; box-sizing: border-box; }
  html, body { width: 1200px; height: 800px; overflow: hidden; }
  body {
    background: var(--page-bg);
    font-family: "Arimo", Arial, sans-serif;
    position: relative;
  }
  .card {
    position: absolute;
    top: 130px;
    width: 350px;
    height: 540px;
    box-shadow: 0 6px 18px rgba(0,0,0,0.18);
  }
  /* Front */
  .card-front {
    left: 225px;
    background: linear-gradient(180deg, var(--teal-top) 0%, var(--teal-mid) 38%, var(--teal-low) 65%, var(--teal-deep) 100%);
    display: flex;
    flex-direction: column;
    align-items: center;
    justify-content: center;
  }
  .brand { text-align: center; color: var(--logo-ink); font-weight: 700; }
  .brand-mark {
    display: block;
    width: 22px; height: 22px;
    margin: 0 auto 18px;
    background: var(--logo-ink);
  }
  .brand-name { font-size: 38px; letter-spacing: 1px; line-height: 1; }
  .brand-rule {
    width: 250px; height: 1px; margin: 8px auto 6px;
    background: var(--logo-ink);
  }
  .brand-tagline { font-size: 13px; letter-spacing: 2.5px; }
  /* Back */
  .card-back {
    left: 625px;
    background: var(--card-white);
    padding: 0 30px 42px;
    display: flex;
    flex-direction: column;
    justify-content: flex-end;
  }
  .person-name { font-size: 22px; font-weight: 700; color: var(--ink); letter-spacing: 0.5px; }
  .person-role { font-size: 17px; color: var(--teal-accent); margin: 2px 0 10px; }
  .contact-list { list-style: none; }
  .contact-item {
    display: flex; align-items: center; gap: 10px;
    font-size: 17px; color: var(--ink-soft); line-height: 1.4;
  }
  .contact-icon { width: 16px; height: 16px; flex: none; fill: var(--teal-accent); }
  .company-name { font-size: 17px; font-weight: 700; color: var(--teal-accent); margin-top: 8px; }
  .company-address { font-size: 17px; color: var(--ink-soft); line-height: 1.35; font-style: normal; }
</style>
</head>
<body>
  <section class="card card-front" aria-label="Card front">
    <div class="brand">
      <span class="brand-mark" aria-hidden="true"></span>
      <div class="brand-name">LANDMERE</div>
      <div class="brand-rule"></div>
      <div class="brand-tagline">Property Investments</div>
    </div>
  </section>

  <section class="card card-back" aria-label="Card back">
    <h1 class="person-name">YOUR NAME</h1>
    <p class="person-role">Director</p>
    <ul class="contact-list">
      <li class="contact-item">
        <svg class="contact-icon" viewBox="0 0 16 16" aria-hidden="true"><path d="M3.5 1l2.5 3-1.4 1.6c.8 1.9 2.2 3.3 4.1 4.2L10.3 8.4l3.2 2.4-1.2 2.9C6.7 13.6 2 9 1.3 3.2z"/></svg>
        <span>123 456 7890</span>
      </li>
      <li class="contact-item">
        <svg class="contact-icon" viewBox="0 0 16 16" aria-hidden="true"><path d="M4 1h7l1 1v3H4zM2 6h12a1 1 0 0 1 1 1v5h-2v3H3v-3H1V7a1 1 0 0 1 1-1zm3 5v3h6v-3z"/></svg>
        <span>123 456 7890</span>
      </li>
      <li class="contact-item">
        <svg class="contact-icon" viewBox="0 0 16 16" aria-hidden="true"><path d="M1 3h14v10H1zm1.5 1.3V5l5.5 4 5.5-4v-.7z"/></svg>
        <span>yourname@landmere.com</span>
      </li>
    </ul>
    <p class="company-name">LANDMERE Property Investments</p>
    <address class="company-address">Suite 123 Harlow Road,<br>Westbury 12345</address>
  </section>
</body>
</html>
```